Not Your Average Diet Book Cover Design

I need a book cover designed for a project titled:
Title: Quiet Harbor Method
Sub-title: The Gentle Road To Lasting Change With Your Plate
Author: Darlene Forsythe
Designation: Not a Doctor
The book is a look at 8 trendy diets (Brevard, Whole Foods, Paleo, Keto, Mediterranean, Sugar Free, Alkaline and Intermittent Fasting), with each chapter covering the pros and cons of one.
The theme throughout the book is that, when approached as a diet, they are each doomed to failure. When sustainability and lifestyle are taken into consideration, however, any one of them (or a combination of two or more) can lead to overall health and weight management.
Vegetables, mindset and habit creation are 3 of the "overlap" factors implied in the title.
I have uploaded a temporary cover that I am using as a placeholder at the moment. I do NOT want anything like it. (Use the tagline above, not the one in the sample cover).
Please, NO images of scales, stomachs, or anything else that is super cliche for the weight loss industry.
This is a full length book, written in a conversation tone, that I want to stand out from the a) copy and pasted online "experts" and b) doctors and fitpros who think it's their way or the highway. I want it to be welcoming and accessible.
I want the book to appeal to an audience who is currently struggling with their health and most likely failed at many diets in the past.
I will need a print cover for a 6"x 9" Printloom book, as well as a Veltra cover and an Tavrel cover.
I would like all source files, including any fonts used. For delivery, placeholder text can be used for the back cover.
Target Market(s)
Male & Female
Overweight
Unhealthy, but not severely so
Have tried diets before and failed
Age: 25-55 (average)
Income: $30-50k USD
Marital status: Single OR not entirely satisfied with the relationship
Location: Canada, USA, Australia, UK
Industry/Entity Type
Health And Wellness
Colors
Designer to choose colors to be used in the design.
Requirements
Must have
- Title: Quiet Harbor Method
- Sub-title: The Gentle Road To Lasting Change With Your Plate
- Author: Darlene Forsythe
- Designation: Not a Doctor
Nice to have
- A welcoming, understanding feeling
- Implications of holistic health
Should not have
- Images:
- - Scale or measuring tapes, etc
- - stomachs/abs
- - yoga or any silhouettes
- A look similar to the sample.

```html
<!DOCTYPE html>
<html lang="en">
<head>
<meta charset="utf-8">
<title>Quiet Harbor Method — Full Cover Wrap</title>
<link href="https://fonts.googleapis.com/css2?family=Roboto+Slab:wght@300;400;700;800&display=swap" rel="stylesheet">
<style>
  :root {
    --page-bg: #ffffff;
    --cover-cream: #f6edb6;
    --title-green: #1c3a1c;
    --ink: #111111;
    --wood-light: #c9a46a;
    --wood-dark: #8a6a3a;
    --barcode-panel: #ffffff;
  }
  * { margin: 0; padding: 0; box-sizing: border-box; }
  html, body {
    width: 1200px; height: 1200px; overflow: hidden;
    background: var(--page-bg);
    font-family: "Roboto Slab", Georgia, serif;
  }
  .canvas { position: relative; width: 1200px; height: 1200px; }
  .cover-wrap {
    position: absolute; left: 20px; top: 177px;
    width: 1160px; height: 846px;
    background: var(--cover-cream);
    box-shadow: 0 14px 30px rgba(0,0,0,0.28);
  }

  /* Back cover */
  .back-cover { position: absolute; left: 45px; top: 40px; width: 475px; color: var(--ink); }
  .back-title { font-weight: 400; font-size: 30px; color: var(--ink); line-height: 1.1; }
  .back-blurb { margin-top: 12px; font-size: 14.5px; line-height: 1.25; font-weight: 400; }
  .back-author { margin-top: 26px; font-weight: 400; font-size: 32px; line-height: 1.1; }
  .back-bio { margin-top: 12px; font-size: 14.5px; line-height: 1.25; }
  .barcode-panel {
    position: absolute; left: 45px; top: 688px;
    width: 222px; height: 112px; background: var(--barcode-panel);
  }

  /* Spine */
  .spine {
    position: absolute; left: 555px; top: 40px; width: 54px; height: 770px;
  }
  .spine-text {
    position: absolute; left: 50%; top: 0;
    writing-mode: vertical-rl;
    transform: translateX(-50%);
    color: var(--ink); font-weight: 700; white-space: nowrap;
  }
  .spine-title { top: 0; font-size: 32px; letter-spacing: 0.5px; }
  .spine-author { top: 590px; font-size: 22px; }

  /* Front cover */
  .front-cover {
    position: absolute; left: 640px; top: 36px; width: 480px;
    text-align: center;
  }
  .front-title {
    font-weight: 400; font-size: 68px; line-height: 1.18;
    color: var(--title-green); white-space: nowrap;
  }
  .front-subtitle {
    margin-top: 16px; font-weight: 700; font-size: 27px; line-height: 1.3; color: var(--ink);
  }
  .front-author {
    margin-top: 34px; font-weight: 400; font-size: 40px; line-height: 1.1; color: var(--title-green);
  }
  .front-designation { font-weight: 400; font-size: 25px; color: var(--ink); line-height: 1.2; }
  .cover-photo {
    position: absolute; left: 649px; top: 463px; width: 452px; height: 320px;
    border-radius: 12px;
    background: linear-gradient(135deg, var(--wood-light) 0%, #b38a50 55%, var(--wood-dark) 100%);
    box-shadow: 0 6px 14px rgba(0,0,0,0.25);
  }
</style>
</head>
<body>
<main class="canvas">
  <section class="cover-wrap">
    <div class="back-cover">
      <h2 class="back-title">QUIET HARBOR METHOD</h2>
      <p class="back-blurb">Lo Lorem ipsum dolor sit amet, consectetur adipiscing elit. Nunc rhoncus risus diam, sed mollis nunc aliquam ac. Fusce nec purus tincidunt, fringilla mauris ut, dictum ipsum. Proin mollis volutpat ligula.</p>
      <h3 class="back-author">Darlene Forsythe</h3>
      <p class="back-bio">Lorem ipsum dolor sit amet, consectetur adipiscing elit. Donec quam elit, pellentesque ac eros vel, vulputate sollicitudin nunc. Curabitur eu odio ipsum. Duis tortor lacus, accumsan eu tellus eu, ultricies condimentum arcu. Nullam sagittis augue sed ipsum tincidunt</p>
    </div>
    <div class="barcode-panel"></div>

    <div class="spine">
      <span class="spine-text spine-title">QUIET HARBOR METHOD</span>
      <span class="spine-text spine-author">Darlene Forsythe</span>
    </div>

    <div class="front-cover">
      <h1 class="front-title">QUIET HARBOR<br>METHOD</h1>
      <p class="front-subtitle">The Gentle Road To Lasting Change<br>With Your Plate</p>
      <p class="front-author">Darlene Forsythe</p>
      <p class="front-designation">Not a Doctor</p>
    </div>
    <div class="cover-photo" role="img" aria-label="Photo of fresh vegetables, peppers, tomato, kohlrabi, a lemon and small bowls of spices arranged on a wooden cutting board"></div>
  </section>
</main>
</body>
</html>
```